Stationery Design

Need a stationery design for an established accounting firm based in London, England.

The company’s name is ‘Harold Brinkley’. We provide a broad range of bookkeeping, accounting, audit, tax and business services to a wide range of clients (ie, individuals, company, partnerships, etc).

The stationary design needs to show strength and trust and should be clean, corporate and professional.

Only 2 colours must be used as noted on the logo.

The fonts are in Optima

We need the following:

#1: Business Cards (design on 2 sides)
#2: Letterhead (word format) and can be sent to printers
#3: Continuation sheets (word format) and can be sent to printers
#4: Sales invoice template (word format) and can be sent to printers
#5: Report Cover front and back for binding,
#6: Complimentary Slips,
#7: Legal corners with our logo only
#7: Email signature templates

I have attached my company's logo in various file formats

We also need to have our accountancy association’s logo and this must be in the same colour as the dark blue. This PQTB logo must be at least 8mm square (can be larger). I have attached the PQTB logo in various file formats

I have also attached other information that you will need for the letter head and invoice templates

I have also attached our old letterhead, fee note template for reference
Updates

Dear Designers - I have increased the budget

Dear Designers - I have read your comments on the fact that the prize does not reflect the work. Thank you and I appreciate your comments. Unfortunately, I am a start up and my budget is limited. As an Alternative, I have reduced the work that I am asking for to the following items and I hope you can assist: #1: Business Cards (design on 2 sides) #2: Letterhead (word format) and can be sent to printers #3: Report Cover front and back for binding, #4: Email signature templates Regards

Industry/Entity Type

Accounting

```html
<!DOCTYPE html>
<html lang="en">
<head>
<meta charset="utf-8">
<title>Harold Brinkley Accountants – Business Card</title>
<link href="https://fonts.googleapis.com/css2?family=Belleza&display=swap" rel="stylesheet">
<style>
  :root {
    --navy: #25406a;
    --plum: #8b3a7e;
    --ink: #3a3f4a;
    --paper: #ffffff;
    --frame: #c8c8c8;
    --label: #8a8a8a;
  }
  * { margin: 0; padding: 0; box-sizing: border-box; }
  html, body { width: 1200px; height: 452px; overflow: hidden; background: var(--paper); }
  body { font-family: "Belleza", "Optima", sans-serif; }

  .sheet {
    position: relative;
    width: 1200px; height: 452px;
    border: 1px solid var(--frame);
  }

  .card { position: absolute; top: 45px; width: 514px; height: 342px; }
  .card--front { left: 56px; background: var(--navy); }
  .card--back { left: 609px; background: var(--paper); border: 1px solid var(--frame); }

  .brand { position: absolute; display: flex; align-items: center; }
  .brand__square { flex: none; }
  .brand__text { text-transform: uppercase; line-height: 1; }
  .brand__name { display: block; }
  .brand__sub { display: block; text-align: right; letter-spacing: 0.22em; }

  .card--front .brand { left: 110px; top: 144px; color: var(--paper); }
  .card--front .brand__square { width: 50px; height: 50px; background: var(--paper); margin-right: 16px; }
  .card--front .brand__name { font-size: 30px; }
  .card--front .brand__sub { font-size: 12px; margin-top: 8px; }

  .card--back .top-band { position: absolute; left: -1px; top: -1px; width: 514px; height: 16px; background: var(--navy); }
  .card--back .brand { left: 29px; top: 43px; color: var(--navy); }
  .card--back .brand__square { width: 40px; height: 40px; background: var(--navy); margin-right: 10px; }
  .card--back .brand__name { font-size: 22px; }
  .card--back .brand__sub { font-size: 9px; margin-top: 5px; }

  .association-badge { position: absolute; left: 439px; top: 30px; width: 55px; height: 55px; background: var(--navy); }

  .person { position: absolute; left: 34px; top: 226px; }
  .person__name {
    font-size: 19px; color: var(--navy); text-transform: uppercase;
    padding-bottom: 3px; border-bottom: 1px solid var(--navy); display: inline-block;
  }
  .person__role { font-size: 17px; color: var(--plum); margin-top: 3px; }

  .contact { position: absolute; left: 226px; top: 224px; font-size: 13px; color: var(--ink); line-height: 17.5px; }
  .contact__lines { margin-bottom: 16px; }

  .side-label { position: absolute; font-size: 21px; color: var(--label); }
  .side-label--front { left: 288px; top: 406px; }
  .side-label--back { left: 840px; top: 413px; }
</style>
</head>
<body>
<main class="sheet">
  <section class="card card--front">
    <div class="brand">
      <span class="brand__square"></span>
      <span class="brand__text">
        <span class="brand__name">Harold Brinkley</span>
        <span class="brand__sub">Accountants</span>
      </span>
    </div>
  </section>

  <section class="card card--back">
    <div class="top-band"></div>
    <div class="brand">
      <span class="brand__square"></span>
      <span class="brand__text">
        <span class="brand__name">Harold Brinkley</span>
        <span class="brand__sub">Accountants</span>
      </span>
    </div>
    <div class="association-badge" role="img" aria-label="Professional association membership badge"></div>

    <div class="person">
      <div class="person__name">Harold Brinkley</div>
      <div class="person__role">Director</div>
    </div>

    <address class="contact" style="font-style: normal;">
      <div class="contact__lines">
        12 Kestrel Court<br>
        Northwick Business Park, Elmstead Road<br>
        Pinner-on-the-Green, Middlesex, HA5 2QT
      </div>
      <div>
        Tel: 020 7946 0321<br>
        web: www.haroldbrinkley.co.uk
      </div>
    </address>
  </section>

  <p class="side-label side-label--front">front</p>
  <p class="side-label side-label--back">back</p>
</main>
</body>
</html>
```